Marketing Software requires Fun and Young Business Card Design

We are looking for a new business card design for a start-up marketing campaign management software that is

- fun
- young/fresh
- engaging
- playful
- new kid on the blog
- wants to catch attention

Check out our website: www.zentripohq.com and watch the first video on the homepage. That way you will get a good picture of the product and the target group.

The current business card (attached) is too mainstream and does not catch the attention that we are looking for.
Attached you will find the company logo, some support images from our website and the current business card design.

Company colours: Zentripo Green
RGB 166 / 176 / 12
CMYK needs conversion

Company font:
Titillium for logo copy
Calibri for content copy

Target Market(s)

- marketing people - design, ad and marketing agency people - main market location: Western Europe and North America

Industry/Entity Type

Marketing

Requirements
Must have
• Information that we would like to have on the BC:
Name: Marcus Pellworth
Function: CEO
Email: marcusp@zentripohq.com
Mobile: +44 7912 584 207
Website: www.zentripohq.com (maybe)
Nice to have
• In the supporting files you will find some images from the website that could be reused but is not essential.
We liked the idea of the origami look and feel however this might not necessarily the winner.
We also like our robot from our video on the website www.zentripohq.com.
A call to action to try our product for free might be nice (get a free trial@www.zentripohq.com)

We are looking forward to seeing something new than the standard business card.

```html
<!DOCTYPE html>
<html lang="en">
<head>
<meta charset="utf-8">
<title>Zentripo Business Card</title>
<link rel="stylesheet" href="https://fonts.googleapis.com/css2?family=Titillium+Web:wght@300;400;700&family=Carlito:wght@400;700&display=swap">
<style>
  :root {
    --backdrop: #6b4127;
    --card: #ffffff;
    --ink: #1f1f1f;
    --ink-soft: #555555;
    --muted: #6e6e6e;
    --green-deep: #3d8a2f;
    --green-mid: #6aa82a;
    --green-lime: #c8dc28;
    --brand-green: #a6b00c;
  }
  * { box-sizing: border-box; margin: 0; padding: 0; }
  html, body { width: 1200px; height: 758px; overflow: hidden; }
  body {
    background: var(--backdrop);
    font-family: "Carlito", "Calibri", sans-serif;
    position: relative;
  }
  .card {
    position: absolute;
    top: 214px;
    width: 540px;
    height: 330px;
    background: var(--card);
    border-radius: 26px;
    overflow: hidden;
    box-shadow: 0 10px 24px rgba(0,0,0,0.35);
  }
  .card--front { left: 40px; }
  .card--back { left: 620px; }

  .brand { position: absolute; left: 44px; top: 58px; }
  .brand__name {
    font-family: "Titillium Web", sans-serif;
    font-weight: 700;
    font-size: 50px;
    line-height: 1;
    color: var(--ink);
    letter-spacing: -0.5px;
  }
  .brand__tagline {
    font-family: "Titillium Web", sans-serif;
    font-weight: 400;
    font-size: 19px;
    color: var(--ink-soft);
    margin-top: 2px;
    margin-left: 4px;
  }

  .contacts { position: absolute; left: 48px; top: 168px; list-style: none; }
  .contacts li {
    display: flex; align-items: center; gap: 8px;
    font-size: 13.5px; color: var(--muted); line-height: 20px;
  }
  .contacts svg { width: 10px; height: 10px; fill: var(--muted); }

  .band { position: absolute; left: 0; top: 0; width: 540px; height: 330px; }

  .holder {
    position: absolute; left: 46px; top: 258px;
    font-weight: 700; font-size: 19px; color: #fff;
  }
  .holder__role { font-weight: 400; font-size: 14px; }

  .back-brand {
    position: absolute; left: 0; right: 0; top: 96px;
    display: flex; justify-content: center; align-items: center; gap: 12px;
  }
  .back-brand__dot { width: 16px; height: 16px; background: var(--brand-green); }
  .back-brand__name {
    font-family: "Titillium Web", sans-serif;
    font-weight: 700; font-size: 58px; color: var(--green-deep); line-height: 1;
  }
  .back-url {
    position: absolute; left: 0; right: 0; top: 236px; text-align: center;
    font-weight: 700; font-size: 24px; letter-spacing: 3.5px; color: var(--ink-soft);
  }
</style>
</head>
<body>
  <section class="card card--front">
    <svg class="band" viewBox="0 0 540 330" aria-hidden="true">
      <defs>
        <linearGradient id="bandGradient" x1="0" x2="1" y1="0" y2="0">
          <stop offset="0" stop-color="var(--green-deep)"/>
          <stop offset="0.45" stop-color="var(--green-mid)"/>
          <stop offset="1" stop-color="var(--green-lime)"/>
        </linearGradient>
        <linearGradient id="stripeGradient" x1="0" x2="1" y1="0" y2="0">
          <stop offset="0" stop-color="#ffffff" stop-opacity="0"/>
          <stop offset="0.5" stop-color="var(--green-mid)"/>
          <stop offset="1" stop-color="var(--green-lime)"/>
        </linearGradient>
      </defs>
      <polygon points="0,250 290,250 290,292 0,292" fill="var(--green-deep)"/>
      <polygon points="160,240 540,194 540,236 230,272" fill="url(#stripeGradient)"/>
    </svg>

    <div class="brand">
      <div class="brand__name">Zentripo</div>
      <div class="brand__tagline">marketing collaboration</div>
    </div>

    <ul class="contacts">
      <li><svg viewBox="0 0 10 10"><rect x="2" y="0" width="6" height="10" rx="1.5"/></svg>+44 7912 584 207</li>
      <li><svg viewBox="0 0 10 10"><rect x="0" y="1.5" width="10" height="7"/></svg>marcusp@zentripohq.com</li>
      <li><svg viewBox="0 0 10 10"><circle cx="5" cy="5" r="5"/></svg>www.zentripohq.com</li>
    </ul>

    <div class="holder">Marcus Pellworth, <span class="holder__role">CEO</span></div>
  </section>

  <section class="card card--back">
    <div class="back-brand">
      <span class="back-brand__dot"></span>
      <span class="back-brand__name">Zentripo</span>
    </div>
    <div class="back-url">www.zentripohq.com</div>
  </section>
</body>
</html>
```